Varnok Develoipment and Management Corp Web Design Project

Website... Based on logo. Update forthcoming....
Updates

Reason: Extended to include recently completed logo design.

Target Market(s)

Financiers, investors, public officials, and landowners.

Industry/Entity Type

Management

Requirements
Should not have
• No palm trees, mayan ruins, or other Caribbean references.

```html
<!DOCTYPE html>
<html lang="en">
<head>
<meta charset="utf-8">
<title>Varnok Development and Management Corp</title>
<link href="https://fonts.googleapis.com/css2?family=Ubuntu:wght@400;500&family=Carlito:wght@400;700&display=swap" rel="stylesheet">
<style>
  :root {
    --green: #a4c43b;
    --green-dark: #8eab2a;
    --slate: #6c7780;
    --slate-dark: #5b656d;
    --navy: #14263d;
    --navy-line: #1d3450;
    --text: #6a7079;
    --heading: #6e747c;
    --white: #ffffff;
    --search: #d3d6d9;
  }
  * { box-sizing: border-box; margin: 0; padding: 0; }
  html, body { width: 689px; height: 1200px; overflow: hidden; background: var(--white); }
  body { position: relative; font-family: "Carlito", "Calibri", sans-serif; color: var(--text); }
  .abs { position: absolute; }
  .heading { font-family: "Ubuntu", sans-serif; font-weight: 400; color: var(--heading); font-size: 21px; }

  /* header */
  .brand { left: 21px; top: 28px; display: flex; align-items: center; gap: 9px; }
  .brand-mark { width: 26px; height: 26px; background: var(--slate); }
  .brand-name { font-family: "Ubuntu", sans-serif; font-weight: 500; font-size: 32px; color: var(--green); letter-spacing: 1px; line-height: 1; }
  .search { left: 320px; top: 38px; width: 169px; height: 24px; border-radius: 8px; background: var(--search); overflow: hidden; display: flex; }
  .search-field { flex: 1; font-family: "Ubuntu", sans-serif; font-style: italic; font-size: 12px; color: var(--white); padding: 5px 9px; }
  .search-btn { width: 32px; background: #c2c6ca; display: flex; align-items: center; justify-content: center; }
  .contact-top { right: 21px; top: 30px; text-align: right; font-family: "Ubuntu", sans-serif; color: var(--heading); }
  .contact-top .phone { font-size: 19px; line-height: 1.1; }
  .contact-top .email { font-size: 11px; }

  /* nav */
  .main-nav { left: 0; top: 89px; width: 689px; height: 29px; background: var(--green); }
  .main-nav ul { list-style: none; display: flex; height: 100%; padding-left: 21px; }
  .main-nav li { font-family: "Ubuntu", sans-serif; font-size: 14px; color: var(--white); line-height: 29px; text-align: center; }
  .main-nav li.current { background: var(--green-dark); color: #2b3320; width: 74px; }
  .main-nav .w1 { width: 94px; } .main-nav .w2 { width: 106px; } .main-nav .w3 { width: 116px; }
  .main-nav .w4 { width: 104px; } .main-nav .w5 { width: 136px; }

  /* hero */
  .hero { left: 0; top: 118px; width: 689px; height: 317px; background: radial-gradient(ellipse at 45% 55%, #1e4a86 0%, #112544 45%, #0b1626 100%); }
  .hero-arrow { top: 136px; }
  .hero-dots { left: 0; width: 689px; display: flex; justify-content: center; gap: 9px; padding-right: 2px; }
  .hero-dots span { width: 12px; height: 12px; border-radius: 50%; background: var(--green); border: 2px solid #e8f0cf; }

  /* welcome */
  .welcome { left: 21px; top: 462px; width: 647px; text-align: center; }
  .welcome p { font-size: 13.5px; line-height: 20px; margin: 12px auto 0; width: 636px; }
  .divider { left: 21px; top: 586px; width: 647px; height: 1px; background: var(--green); }

  /* services */
  .services { left: 21px; top: 613px; width: 300px; }
  .services ul { list-style: none; margin-top: 6px; }
  .services li { font-size: 14px; line-height: 20.5px; display: flex; align-items: center; gap: 3px; }

  .testimonial { left: 21px; top: 778px; width: 290px; }
  .testimonial-nav { left: 278px; top: 784px; display: flex; gap: 6px; }
  .testimonial p { font-size: 14px; line-height: 17.5px; margin-top: 10px; }

  /* projects */
  .projects { left: 391px; top: 613px; width: 277px; }
  .project { position: absolute; left: 0; width: 277px; height: 67px; display: flex; }
  .project-photo { width: 69px; height: 67px; }
  .project-body { flex: 1; padding: 4px 12px 0 13px; color: var(--white); font-size: 11.5px; line-height: 14px; position: relative; }
  .project-body .more { position: absolute; right: 12px; bottom: 3px; font-weight: 700; font-size: 13px; }
  .project.green .project-body { background: var(--green); }
  .project.grey .project-body { background: var(--slate); }

  /* footer band */
  .info-band { left: 0; top: 934px; width: 689px; height: 197px; background: var(--slate); border-top: 2px solid var(--navy-line); }
  .band-title { font-family: "Ubuntu", sans-serif; font-weight: 400; font-size: 20px; color: var(--green); }
  .map { left: 21px; top: 982px; width: 275px; height: 130px; border: 2px solid var(--white); background: linear-gradient(135deg, #e6e2d8 0%, #d8d9cf 45%, #b6cbe6 55%, #e4e0d4 100%); }
  .address { left: 328px; top: 980px; color: var(--white); font-size: 14px; line-height: 17px; font-style: normal; }
  .phones { right: 21px; top: 980px; color: var(--white); font-size: 14px; line-height: 17px; text-align: right; }
  .newsletter-label { left: 328px; top: 1060px; color: var(--white); font-size: 14px; }
  .newsletter { left: 328px; top: 1081px; width: 340px; height: 30px; display: flex; }
  .newsletter-field { flex: 1; background: #7d8891; color: #c7cdd2; font-style: italic; font-size: 13.5px; padding: 6px 16px; }
  .newsletter-btn { width: 110px; background: var(--slate-dark); color: var(--white); font-style: italic; font-size: 14px; text-align: center; line-height: 30px; }

  /* bottom bar */
  .bottom-bar { left: 0; top: 1131px; width: 689px; height: 69px; background: var(--navy); border-top: 2px solid var(--green); }
  .footer-nav { left: 21px; top: 1146px; font-family: "Ubuntu", sans-serif; font-size: 10.5px; color: var(--white); }
  .footer-nav .current { color: var(--green); }
  .copyright { left: 21px; top: 1172px; font-size: 9px; color: var(--white); }
  .social { left: 523px; top: 1146px; display: flex; gap: 5px; }
  .social span { width: 25px; height: 25px; border-radius: 50%; }
  .s1 { background: #3b5d9a; } .s2 { background: #2aa4df; } .s3 { background: #1b7cb5; } .s4 { background: #d9402f; } .s5 { background: #ef7d22; }
</style>
</head>
<body>

<header>
  <div class="abs brand"><span class="brand-mark"></span><span class="brand-name">VARNOK</span></div>
  <div class="abs search">
    <span class="search-field">Search our site...</span>
    <span class="search-btn">
      <svg width="14" height="14" viewBox="0 0 14 14"><circle cx="6" cy="6" r="4.2" fill="none" stroke="#fff" stroke-width="1.6"/><line x1="9" y1="9" x2="13" y2="13" stroke="#fff" stroke-width="1.8"/></svg>
    </span>
  </div>
  <div class="abs contact-top">
    <div class="phone">01234 567890</div>
    <div class="email">email: name@domain.com</div>
  </div>
</header>

<nav class="abs main-nav">
  <ul>
    <li class="current">HOME</li><li class="w1">ABOUT</li><li class="w2">SERVICES</li><li class="w3">OUR TEAM</li><li class="w4">NEWS</li><li class="w5">CONTACT US</li>
  </ul>
</nav>

<section class="abs hero" role="img" aria-label="Businessman drawing a rising glowing blue growth chart">
  <svg class="abs hero-arrow" style="left:21px" width="26" height="44" viewBox="0 0 26 44"><polyline points="24,1 2,22 24,43" fill="none" stroke="#fff" stroke-width="2"/></svg>
  <svg class="abs hero-arrow" style="right:21px" width="26" height="44" viewBox="0 0 26 44"><polyline points="2,1 24,22 2,43" fill="none" stroke="#fff" stroke-width="2"/></svg>
  <div class="abs hero-dots" style="top:295px"><span></span><span></span><span></span><span></span></div>
</section>

<section class="abs welcome">
  <h1 class="heading">Welcome to Varnok Development and Management Corp</h1>
  <p>Lorem Ipsum is simply dummy text of the printing and typesetting industry. Lorem Ipsum has been the industry's standard dummy text ever since the 1500s, when an unknown printer took a galley of type and scrambled it to make a type specimen book. LayoutDesk including versions of Lorem Ipsum.</p>
</section>
<div class="abs divider"></div>

<section class="abs services">
  <h2 class="heading">What we do</h2>
  <ul>
    <li><svg width="12" height="12" viewBox="0 0 12 12"><polyline points="1,6 4.5,10 11,1" fill="none" stroke="#a4c43b" stroke-width="2"/></svg>Service you provide goes here</li>
    <li><svg width="12" height="12" viewBox="0 0 12 12"><polyline points="1,6 4.5,10 11,1" fill="none" stroke="#a4c43b" stroke-width="2"/></svg>Service you provide goes here</li>
    <li><svg width="12" height="12" viewBox="0 0 12 12"><polyline points="1,6 4.5,10 11,1" fill="none" stroke="#a4c43b" stroke-width="2"/></svg>Service you provide goes here</li>
    <li><svg width="12" height="12" viewBox="0 0 12 12"><polyline points="1,6 4.5,10 11,1" fill="none" stroke="#a4c43b" stroke-width="2"/></svg>Service you provide goes here</li>
    <li><svg width="12" height="12" viewBox="0 0 12 12"><polyline points="1,6 4.5,10 11,1" fill="none" stroke="#a4c43b" stroke-width="2"/></svg>Service you provide goes here</li>
  </ul>
</section>

<section class="abs testimonial">
  <h2 class="heading">What our clients say</h2>
  <p>“Lorem Ipsum is simply dummy text of the printing and typesetting industry. Lorem Ipsum has been the industry's standard dummy text ever since the 1500s, when an unknown printer took a galley...”</p>
</section>
<div class="abs testimonial-nav">
  <svg width="10" height="18" viewBox="0 0 10 18"><polyline points="9,1 1,9 9,17" fill="none" stroke="#a4c43b" stroke-width="1.5"/></svg>
  <svg width="10" height="18" viewBox="0 0 10 18"><polyline points="1,1 9,9 1,17" fill="none" stroke="#a4c43b" stroke-width="1.5"/></svg>
</div>

<section class="abs projects">
  <h2 class="heading">Recent projects</h2>
  <article class="project green" style="top:38px">
    <div class="project-photo" role="img" aria-label="Photo of a smiling couple at a meeting" style="background:linear-gradient(135deg,#c9c2b6,#6f7d8c)"></div>
    <div class="project-body">Lorem Ipsum is simply dummy text of the printing and typesetting industry. Lorem Ipsum has...<span class="more">read more</span></div>
  </article>
  <article class="project grey" style="top:125px">
    <div class="project-photo" role="img" aria-label="Photo of hands holding coins with a young plant" style="background:linear-gradient(180deg,#bfe0f2,#d9b596 60%,#6fa343)"></div>
    <div class="project-body">Lorem Ipsum is simply dummy text of the printing and typesetting industry. Lorem Ipsum has...<span class="more">read more</span></div>
  </article>
  <article class="project green" style="top:214px">
    <div class="project-photo" role="img" aria-label="Photo of a model house" style="background:linear-gradient(160deg,#eeeae4,#a48769 70%,#7d6a57)"></div>
    <div class="project-body">Lorem Ipsum is simply dummy text of the printing and typesetting industry. Lorem Ipsum has...<span class="more">read more</span></div>
  </article>
</section>

<footer>
  <div class="abs info-band"></div>
  <h3 class="abs band-title" style="left:21px;top:948px">How to find us</h3>
  <div class="abs map" role="img" aria-label="Street map showing the office location"></div>
  <h3 class="abs band-title" style="left:328px;top:948px">Contact us</h3>
  <address class="abs address">Address line one<br>Address line two<br>Address line three<br>Address line four</address>
  <div class="abs phones">Telephone: 01234 567890<br>Fax: 01234 567890<br>name@yourdomain.com<br>name@yourdomain.com</div>
  <div class="abs newsletter-label">Sign up to our newsletter</div>
  <div class="abs newsletter">
    <span class="newsletter-field">please enter your email address</span>
    <span class="newsletter-btn">Register</span>
  </div>

  <div class="abs bottom-bar"></div>
  <div class="abs footer-nav"><span class="current">HOME</span> / ABOUT / SERVICES &nbsp;/ OUR TEAM / NEWS / CONTACT US</div>
  <div class="abs copyright">© 2014 Company name here</div>
  <div class="abs social"><span class="s1"></span><span class="s2"></span><span class="s3"></span><span class="s4"></span><span class="s5"></span></div>
</footer>

</body>
</html>
```